Invesment management business need a stationery design

We need a stationery design for a new company based in Sao Paulo, Brazil, called "Tressily Capital". We provide investment management services for individuals and corporations.
The final design should communicate financial safety and some kind of luxury, just like an investment bank does.
As an inspiration, the designer could take a look at companies like KT Halbrook, Whitcombe Fairley, NKV or Banque Orvelle

Target Market(s)

Individuals and corporations

Industry/Entity Type

Business

Requirements
Must have
• My project must have our logo on it.
• Our business cards should have our contact information, such as telephone number and emails.

```html
<!DOCTYPE html>
<html lang="en">
<head>
<meta charset="utf-8">
<title>Tressily Capital – Business Card</title>
<link rel="stylesheet" href="https://fonts.googleapis.com/css2?family=Cinzel:wght@400;500&family=Lato:wght@400;700&display=swap">
<style>
  :root {
    --backdrop: #2b2b2b;
    --card-white: #fbfbfb;
    --card-shade: #e9e9e9;
    --band-grey: #5f5f5f;
    --band-dark: #4a4a4a;
    --brand-grey: #8a8a8a;
    --label-ink: #1f1f1f;
    --value-ink: #5a5a5a;
    --name-ink: #1c1c1c;
    --title-ink: #f2f2f2;
    --accent-gold: #c9a44a;
  }
  * { box-sizing: border-box; margin: 0; padding: 0; }
  html, body {
    width: 1200px;
    height: 999px;
    overflow: hidden;
    background: var(--backdrop);
  }
  .canvas {
    position: relative;
    width: 1200px;
    height: 999px;
  }
  .card {
    position: absolute;
    width: 560px;
    height: 320px;
    border-radius: 22px;
    overflow: hidden;
    background: linear-gradient(160deg, var(--card-white) 0%, var(--card-white) 55%, var(--card-shade) 100%);
    box-shadow: 0 18px 40px rgba(0,0,0,0.55);
  }

  /* Front */
  .card-front { left: 90px; top: 110px; }
  .card-front .brand {
    position: absolute;
    left: 0; right: 0; top: 104px;
    display: flex;
    align-items: center;
    justify-content: center;
    gap: 16px;
  }
  .card-front .footer-band {
    position: absolute;
    left: 0; right: 0; bottom: 0;
    height: 58px;
    background: linear-gradient(180deg, var(--band-grey), var(--band-dark));
  }

  /* Brand lockup */
  .brand-dot {
    width: 30px; height: 30px;
    border-radius: 50%;
    background: var(--accent-gold);
    flex: none;
  }
  .brand-name {
    font-family: "Cinzel", serif;
    font-weight: 400;
    font-size: 38px;
    letter-spacing: 3px;
    color: var(--brand-grey);
    white-space: nowrap;
  }

  /* Back */
  .card-back { left: 550px; top: 520px; }
  .card-back .header-band {
    position: absolute;
    left: 0; right: 0; top: 0;
    height: 62px;
    background: linear-gradient(180deg, var(--band-grey), var(--band-dark));
  }
  .holder {
    position: absolute;
    right: 26px; top: 10px;
    text-align: right;
    font-family: "Cinzel", serif;
  }
  .holder-name {
    font-size: 19px;
    font-weight: 500;
    letter-spacing: 1.5px;
    color: var(--name-ink);
  }
  .holder-title {
    font-size: 14px;
    letter-spacing: 1.5px;
    color: var(--title-ink);
  }
  .card-back .brand {
    position: absolute;
    left: 34px; top: 104px;
    display: flex;
    align-items: center;
    gap: 14px;
  }
  .card-back .brand-name { font-size: 31px; }
  .card-back .brand-dot { width: 26px; height: 26px; }
  .contact {
    position: absolute;
    left: 34px; bottom: 28px;
    list-style: none;
    font-family: "Lato", sans-serif;
    font-size: 19px;
    line-height: 34px;
  }
  .contact-label { font-weight: 700; color: var(--label-ink); }
  .contact-value { font-weight: 400; color: var(--value-ink); }
</style>
</head>
<body>
<main class="canvas">

  <section class="card card-front" aria-label="Business card front">
    <div class="brand">
      <span class="brand-dot"></span>
      <span class="brand-name">Tressily Capital</span>
    </div>
    <div class="footer-band"></div>
  </section>

  <section class="card card-back" aria-label="Business card back">
    <div class="header-band"></div>
    <div class="holder">
      <p class="holder-name">Lívia Moraes</p>
      <p class="holder-title">Designação</p>
    </div>
    <div class="brand">
      <span class="brand-dot"></span>
      <span class="brand-name">Tressily Capital</span>
    </div>
    <ul class="contact">
      <li><span class="contact-label">Telephone:</span> <span class="contact-value">+55 11 940263187</span></li>
      <li><span class="contact-label">Email:</span> <span class="contact-value">lmoraes@tressily.com.br</span></li>
      <li><span class="contact-label">Web:</span> <span class="contact-value">www.tressily.com</span></li>
    </ul>
  </section>

</main>
</body>
</html>
```